Harborview Wellness Counseling
7 business cards, letterhead, envlp, fax cover
Harborview Wellness Counseling -
Creative Brief
Professional
Martin Oakridge
Owner/Manager
2875 Pellham Ridge Blvd. Suite 204 O'Fallon, MO 63412
oakridgehome@brisknet-mail.net
I need cards for each of my seven therapists. I will upload word file with their names and info. Letterhead should not use therapists names.

```html
<!DOCTYPE html>
<html lang="en">
<head>
<meta charset="utf-8">
<title>Harborview Wellness Counseling – Business Card</title>
<link rel="stylesheet" href="https://fonts.googleapis.com/css2?family=Arimo:wght@400;700&display=swap">
<style>
  :root {
    --card-bg: #ffffff;
    --page-bg: #ffffff;
    --ink: #111111;
    --brand-navy: #1f2f5c;
    --brand-orange: #f0a21c;
    --band-red: #e0301e;
    --band-orange: #f36f21;
    --band-yellow: #f9c23c;
    --card-edge: #d9d9d9;
  }
  html, body {
    margin: 0;
    padding: 0;
    width: 1200px;
    height: 686px;
    overflow: hidden;
    background: var(--page-bg);
  }
  .card {
    position: relative;
    width: 1200px;
    height: 686px;
    box-sizing: border-box;
    border: 2px solid var(--card-edge);
    background: var(--card-bg);
    font-family: "Arimo", Arial, sans-serif;
    color: var(--ink);
  }
  .brand {
    position: absolute;
    left: 44px;
    top: 92px;
    width: 580px;
    display: flex;
    align-items: center;
    gap: 14px;
  }
  .brand-dot {
    flex: none;
    width: 34px;
    height: 34px;
    border-radius: 50%;
    background: var(--brand-orange);
  }
  .brand-name {
    font-size: 24px;
    font-weight: 700;
    color: var(--brand-navy);
    letter-spacing: 0;
    white-space: nowrap;
  }
  .accent-band {
    position: absolute;
    left: 640px;
    top: 96px;
    width: 558px;
    height: 38px;
  }
  .contact {
    position: absolute;
    left: 43px;
    top: 436px;
    font-size: 29px;
    line-height: 36px;
  }
  .contact p { margin: 0; }
  .contact .address { margin-top: 22px; }
  .contact .email { margin-top: 8px; }
  .contact .label { display: inline-block; width: 70px; }
  .person {
    position: absolute;
    right: 41px;
    top: 566px;
    text-align: right;
    font-size: 29px;
    line-height: 41px;
  }
  .person p { margin: 0; }
  .person .name { font-weight: 700; }
</style>
</head>
<body>
  <div class="card">
    <div class="brand">
      <span class="brand-dot"></span>
      <span class="brand-name">HARBORVIEW WELLNESS COUNSELING</span>
    </div>

    <svg class="accent-band" viewBox="0 0 558 38" preserveAspectRatio="none" aria-hidden="true">
      <defs>
        <linearGradient id="bandTop" x1="0" y1="0" x2="1" y2="0">
          <stop offset="0" stop-color="#ffffff"/>
          <stop offset="0.35" stop-color="#f6c2b8"/>
          <stop offset="0.7" stop-color="#e0301e"/>
          <stop offset="1" stop-color="#f36f21"/>
        </linearGradient>
        <linearGradient id="bandBottom" x1="0" y1="0" x2="1" y2="0">
          <stop offset="0" stop-color="#ffffff"/>
          <stop offset="0.4" stop-color="#fbe2b0"/>
          <stop offset="1" stop-color="#f9c23c"/>
        </linearGradient>
      </defs>
      <rect x="0" y="0" width="558" height="25" fill="url(#bandTop)"/>
      <rect x="0" y="25" width="558" height="13" fill="url(#bandBottom)"/>
    </svg>

    <div class="contact">
      <p><span class="label">Ph:</span> 636-555-0147</p>
      <p><span class="label">Fax:</span>636-555-0182</p>
      <p class="address">2875 Pellham Ridge Blvd.,</p>
      <p>Suite 204, O'Fallon, MO 63412</p>
      <p class="email">oakridgehome@brisknet-mail.net</p>
    </div>

    <div class="person">
      <p class="name">Martin Oakridge</p>
      <p class="title">Owner/Manager</p>
    </div>
  </div>
</body>
</html>
```